Business card design for new, innovative company - BoldHarbor

We are a new company looking for a business card design that is fun, different and quirky. Must use corporate colour green - CMYK C:55, M:0, Y:100, K:0, and corporate colour grey - C:0, M:0, Y: 0, K:70.

We have developed the first real time data application, in which people are able to profile the data of their existing customers in order to pull out more good fit clients to direct their marketing activities at.

Industry/Entity Type

Marketing

Requirements
Must have
• Logo, name, title, telephone number, fax number, email, website, address

```html
<!DOCTYPE html>
<html lang="en">
<head>
<meta charset="utf-8">
<title>BoldHarbor Business Card</title>
<link href="https://fonts.googleapis.com/css2?family=Arimo:wght@400;700&display=swap" rel="stylesheet">
<style>
  :root {
    --brand-green: #72b62e;
    --brand-grey: #6d6e71;
    --card-dark: #58595b;
    --card-dark-edge: #434446;
    --card-white: #ffffff;
    --text-dark: #3a3a3a;
    --backdrop: #e6e6e4;
  }
  * { margin: 0; padding: 0; box-sizing: border-box; }
  html, body {
    width: 1200px; height: 871px; overflow: hidden;
    background: var(--backdrop);
    font-family: "Arimo", Arial, sans-serif;
  }
  .canvas { position: relative; width: 1200px; height: 871px; }

  .card {
    position: absolute;
    width: 620px; height: 354px;
    border-radius: 3px;
    box-shadow: 0 14px 30px rgba(0,0,0,0.28);
    overflow: hidden;
  }

  /* Front side */
  .card-front {
    left: 90px; top: 90px;
    background: linear-gradient(135deg, var(--card-dark) 0%, var(--card-dark-edge) 100%);
  }
  .card-front .accent-band { position: absolute; left: 0; top: 0; width: 100%; height: 100%; }
  .card-front .wordmark {
    position: absolute; left: 300px; top: 140px;
    font-weight: 700; font-size: 48px; letter-spacing: -1px;
    color: #e9e9e9;
  }

  /* Back side */
  .card-back {
    left: 490px; top: 420px;
    background: linear-gradient(120deg, var(--card-white) 55%, #ececec 100%);
  }
  .card-back .logo-row {
    position: absolute; left: 44px; top: 34px;
    display: flex; align-items: center; gap: 12px;
  }
  .card-back .logo-square { width: 26px; height: 26px; background: var(--brand-green); }
  .card-back .wordmark {
    font-weight: 700; font-size: 50px; letter-spacing: -1px;
    color: var(--brand-grey);
  }
  .card-back .person-name {
    position: absolute; left: 44px; top: 112px;
    font-weight: 700; font-size: 19px; color: var(--brand-green);
  }
  .contact-list {
    position: absolute; left: 44px; top: 150px;
    list-style: none;
  }
  .contact-list li {
    display: flex; align-items: center; gap: 22px;
    height: 26px; font-size: 15px; color: var(--text-dark);
  }
  .contact-list svg { width: 14px; height: 14px; flex: none; }
  .address {
    position: absolute; left: 44px; top: 270px;
    font-size: 15px; color: var(--text-dark);
  }
  .divider {
    position: absolute; left: 44px; top: 298px;
    width: 400px; height: 1px; background: var(--brand-green);
  }
</style>
</head>
<body>
<main class="canvas">

  <section class="card card-front" aria-label="Business card front">
    <svg class="accent-band" viewBox="0 0 620 354" preserveAspectRatio="none" aria-hidden="true">
      <polygon points="0,0 240,0 300,354 0,354" fill="rgba(255,255,255,0.03)"/>
      <polygon points="0,0 220,0 165,250 0,150" fill="var(--brand-green)"/>
    </svg>
    <div class="wordmark">BoldHarbor</div>
  </section>

  <section class="card card-back" aria-label="Business card back">
    <div class="logo-row">
      <span class="logo-square"></span>
      <span class="wordmark">BoldHarbor</span>
    </div>
    <div class="person-name">Nadia Corwell</div>
    <ul class="contact-list">
      <li>
        <svg viewBox="0 0 14 14" aria-hidden="true"><rect x="3.5" y="1" width="7" height="12" rx="1.5" fill="none" stroke="var(--brand-green)" stroke-width="1.4"/><circle cx="7" cy="10.8" r="0.9" fill="var(--brand-green)"/></svg>
        <span>M: 07000 555218</span>
      </li>
      <li>
        <svg viewBox="0 0 14 14" aria-hidden="true"><path d="M2 5 Q7 1 12 5 L10.5 6.5 L9 5.2 L5 5.2 L3.5 6.5 Z" fill="var(--brand-green)"/><rect x="3" y="7" width="8" height="5" rx="1" fill="none" stroke="var(--brand-green)" stroke-width="1.3"/></svg>
        <span>T: 01000 555472</span>
      </li>
      <li>
        <svg viewBox="0 0 14 14" aria-hidden="true"><rect x="1.5" y="3" width="11" height="8" fill="none" stroke="var(--brand-green)" stroke-width="1.3"/><path d="M1.5 3 L7 8 L12.5 3" fill="none" stroke="var(--brand-green)" stroke-width="1.3"/></svg>
        <span>E: nadia.corwell@boldharbordata.com</span>
      </li>
      <li>
        <svg viewBox="0 0 14 14" aria-hidden="true"><circle cx="7" cy="7" r="5.5" fill="none" stroke="var(--brand-green)" stroke-width="1.3"/><ellipse cx="7" cy="7" rx="2.3" ry="5.5" fill="none" stroke="var(--brand-green)" stroke-width="1.1"/><line x1="1.5" y1="7" x2="12.5" y2="7" stroke="var(--brand-green)" stroke-width="1.1"/></svg>
        <span>www.boldharbor.com</span>
      </li>
    </ul>
    <div class="address">22 Quayside Lane, Elmford, Northshire, NP4 7QR</div>
    <div class="divider"></div>
  </section>

</main>
</body>
</html>
```